Business Card, Stationary, and Invoice
PuzzleHarbor
Business Card, Stationary, and Invoice - Games
Creative Brief
Use specific fonts
Use logo font..or similar if logo font doesn't look good.
Bright & Fun-filled
Lyle Ostrand
Owner
84 Brackett Lane Monroe, NY 10953
lyle@puzzleharbor-example.com
www.puzzleharbor-example.com
Require business card, stationary, and invoice.

```html
<!DOCTYPE html>
<html lang="en">
<head>
<meta charset="utf-8">
<title>PuzzleHarbor Business Card</title>
<link rel="stylesheet" href="https://fonts.googleapis.com/css2?family=Open+Sans:wght@400;600;800&display=swap">
<style>
  :root {
    --backdrop: #e9e4dc;
    --card: #ffffff;
    --brand: #3a2c1c;
    --ink: #4a4038;
    --band-dark: #2b2118;
    --band-mid: #5a4630;
    --gold: #c9a96a;
    --gold-light: #e6d3a4;
    --light-text: #ffffff;
  }
  html, body {
    margin: 0;
    padding: 0;
    width: 1200px;
    height: 463px;
    overflow: hidden;
    background: var(--backdrop);
    font-family: "Open Sans", Arial, sans-serif;
  }
  .sheet {
    position: relative;
    width: 1200px;
    height: 463px;
  }
  .card {
    position: absolute;
    top: 69px;
    width: 510px;
    height: 325px;
    background: var(--card);
    border-radius: 22px;
    overflow: hidden;
    box-shadow: 0 3px 10px rgba(0,0,0,0.18);
  }
  .card--front { left: 67px; }
  .card--back { left: 623px; }
  .band {
    position: absolute;
    left: 0;
    top: 0;
    width: 510px;
    height: 325px;
  }
  .brand-name {
    position: absolute;
    margin: 0;
    font-weight: 800;
    line-height: 1;
    color: var(--brand);
    letter-spacing: -0.5px;
    white-space: nowrap;
  }
  .card--front .brand-name { left: 30px; top: 94px; font-size: 30px; }
  .card--back .brand-name { left: 0; right: 0; top: 98px; text-align: center; font-size: 44px; }
  .brand-mark {
    display: inline-block;
    width: 16px;
    height: 16px;
    border-radius: 50%;
    background: var(--gold);
    margin-right: 8px;
    vertical-align: middle;
    position: relative;
    top: -3px;
  }
  .card--back .brand-mark { width: 18px; height: 18px; }
  .contact {
    position: absolute;
    left: 300px;
    top: 52px;
    margin: 0;
    font-size: 10.5px;
    line-height: 1.45;
    color: var(--ink);
    font-style: normal;
  }
  .contact .label { display: inline-block; width: 12px; font-weight: 600; }
  .person {
    position: absolute;
    left: 30px;
    bottom: 32px;
    margin: 0;
    color: var(--light-text);
    font-size: 17px;
    font-weight: 600;
  }
  .person .role {
    font-weight: 400;
    font-size: 14px;
  }
  .person .divider { opacity: 0.7; margin: 0 6px; font-weight: 400; }
  .website {
    position: absolute;
    left: 30px;
    top: 200px;
    margin: 0;
    font-size: 12px;
    color: var(--ink);
  }
  .website strong { font-weight: 600; color: var(--brand); }
</style>
</head>
<body>
<main class="sheet">

  <section class="card card--front">
    <svg class="band" viewBox="0 0 510 325" aria-hidden="true">
      <defs>
        <linearGradient id="bandFront" x1="0" y1="0" x2="1" y2="0">
          <stop offset="0" stop-color="var(--band-dark)"/>
          <stop offset="0.55" stop-color="var(--band-mid)"/>
          <stop offset="1" stop-color="var(--band-dark)"/>
        </linearGradient>
      </defs>
      <path d="M0 250 C 140 270, 330 250, 510 205 L510 325 L0 325 Z" fill="var(--gold-light)"/>
      <path d="M0 262 C 150 282, 340 258, 510 220 L510 325 L0 325 Z" fill="url(#bandFront)"/>
      <path d="M0 256 C 150 276, 335 254, 510 212" fill="none" stroke="var(--gold)" stroke-width="2"/>
    </svg>
    <h1 class="brand-name"><span class="brand-mark"></span>PuzzleHarbor</h1>
    <address class="contact">
      84 Brackett Lane<br>
      Monroe, NY 10953<br>
      <span class="label">C</span>: 845-555-0172<br>
      <span class="label">E</span>: lyle@puzzleharbor-example.com<br>
      <span class="label">W</span>: www.puzzleharbor-example.com
    </address>
    <p class="person">Lyle Ostrand<span class="divider">|</span><span class="role">Owner</span></p>
  </section>

  <section class="card card--back">
    <svg class="band" viewBox="0 0 510 325" aria-hidden="true">
      <defs>
        <linearGradient id="bandBack" x1="0" y1="0" x2="1" y2="0">
          <stop offset="0" stop-color="var(--band-dark)"/>
          <stop offset="0.55" stop-color="var(--band-mid)"/>
          <stop offset="1" stop-color="var(--band-dark)"/>
        </linearGradient>
      </defs>
      <path d="M0 250 C 140 270, 330 250, 510 205 L510 325 L0 325 Z" fill="var(--gold-light)"/>
      <path d="M0 262 C 150 282, 340 258, 510 220 L510 325 L0 325 Z" fill="url(#bandBack)"/>
      <path d="M0 256 C 150 276, 335 254, 510 212" fill="none" stroke="var(--gold)" stroke-width="2"/>
    </svg>
    <h2 class="brand-name"><span class="brand-mark"></span>PuzzleHarbor</h2>
    <p class="website">www.<strong>puzzleharbor-example</strong>.com</p>
  </section>

</main>
</body>
</html>
```